Need Flyer for Our Real estate Agency

Need to run General Campaign for our agency with Start of New Year as our theme ..Must have an agent's picture on the DL..
Address:
27 / 348Marlow rd, Ashvale VIC 3047
Ph:03 9412 7305
email:info@koralinrealestate.com.au
www.koralinrealestate.com.au
Something like as attached picture..
Target Market(s)
Home Buyers
Industry/Entity Type
Real Estate Agent
Requirements
Must have
- Our Logo Colours

```html
<!DOCTYPE html>
<html lang="en">
<head>
<meta charset="utf-8">
<title>Koralin Real Estate – DL Flyer</title>
<link href="https://fonts.googleapis.com/css2?family=Montserrat:wght@400;500;700&display=swap" rel="stylesheet">
<style>
  :root {
    --navy: #1d2450;
    --white: #ffffff;
    --backdrop: #e4e4e4;
    --photo-light: #f1f2f3;
    --photo-mid: #d4d6d9;
    --photo-dark: #3a3d45;
    --text-soft: #e6e8f0;
  }
  * { box-sizing: border-box; margin: 0; padding: 0; }
  html, body {
    width: 1200px;
    height: 1000px;
    overflow: hidden;
    background: var(--backdrop);
    font-family: "Montserrat", Arial, sans-serif;
  }
  .flyer {
    position: absolute;
    left: 50px;
    top: 240px;
    width: 1100px;
    height: 520px;
    display: flex;
    box-shadow: 0 6px 24px rgba(0,0,0,0.12);
  }
  .flyer__panel {
    position: relative;
    width: 640px;
    height: 100%;
    background: var(--navy);
    color: var(--white);
  }
  .brand {
    position: absolute;
    top: 68px;
    left: 0;
    width: 100%;
    text-align: center;
  }
  .brand__row {
    display: inline-flex;
    align-items: center;
    gap: 12px;
  }
  .brand__mark {
    width: 12px;
    height: 12px;
    background: var(--white);
  }
  .brand__name {
    font-size: 40px;
    font-weight: 500;
    letter-spacing: 6px;
  }
  .brand__tag {
    margin-top: 6px;
    font-size: 10px;
    font-weight: 500;
    letter-spacing: 3px;
    border-top: 1px solid var(--white);
    display: inline-block;
    padding-top: 5px;
    width: 230px;
  }
  .quote {
    position: absolute;
    top: 180px;
    left: 20px;
    right: 20px;
    text-align: center;
    font-size: 24px;
    font-weight: 700;
    line-height: 1.25;
    text-transform: uppercase;
    letter-spacing: 0.4px;
    white-space: nowrap;
  }
  .contact {
    position: absolute;
    font-size: 15px;
    color: var(--text-soft);
    display: flex;
    flex-direction: column;
    gap: 8px;
  }
  .contact--left { left: 40px; bottom: 58px; }
  .contact--right { left: 360px; bottom: 30px; }
  .contact__item {
    display: flex;
    align-items: center;
    gap: 8px;
    white-space: nowrap;
  }
  .contact__icon { width: 18px; height: 18px; flex: none; }
  .flyer__photo {
    flex: 1;
    height: 100%;
    background:
      radial-gradient(ellipse 45% 60% at 55% 65%, rgba(43,46,53,0.85) 0%, rgba(43,46,53,0.4) 55%, rgba(43,46,53,0) 100%),
      linear-gradient(180deg, var(--photo-light) 0%, var(--photo-mid) 100%);
  }
</style>
</head>
<body>
  <section class="flyer">
    <div class="flyer__panel">
      <div class="brand">
        <div class="brand__row">
          <span class="brand__mark"></span>
          <span class="brand__name">KORALIN</span>
        </div>
        <div><span class="brand__tag">REAL ESTATE</span></div>
      </div>

      <p class="quote">There have been few things in my life<br>which have had a more genial effect<br>on my mind than the possession of a<br>piece of land.</p>

      <div class="contact contact--left">
        <div class="contact__item">
          <svg class="contact__icon" viewBox="0 0 20 20"><path d="M10 2 1 10h3v8h4v-5h4v5h4v-8h3z" fill="#fff"/></svg>
          27 / 348Marlow rd, Ashvale VIC 3047
        </div>
        <div class="contact__item">
          <svg class="contact__icon" viewBox="0 0 20 20"><rect x="0" y="0" width="20" height="20" rx="3" fill="#fff"/><path d="M6 4c1 0 2 2.5 2 3s-1 1-1 1.5c.5 1.5 2 3 3.5 3.5.5 0 1-1 1.5-1s3 1 3 2-1 2.5-2.5 2.5C8 15.5 4.5 12 4.5 6.5 4.5 5 5 4 6 4z" fill="#1d2450"/></svg>
          03 9412 7305
        </div>
      </div>

      <div class="contact contact--right">
        <div class="contact__item">
          <svg class="contact__icon" viewBox="0 0 20 20"><rect x="1" y="4" width="18" height="12" fill="#fff"/><path d="M1 4l9 7 9-7" stroke="#1d2450" stroke-width="1.5" fill="none"/></svg>
          info@koralinrealestate.com.au
        </div>
        <div class="contact__item">
          <svg class="contact__icon" viewBox="0 0 20 20"><circle cx="10" cy="10" r="8.5" fill="none" stroke="#fff" stroke-width="1.6"/><ellipse cx="10" cy="10" rx="3.5" ry="8.5" fill="none" stroke="#fff" stroke-width="1.4"/><path d="M1.5 10h17M3 6h14M3 14h14" stroke="#fff" stroke-width="1.2"/></svg>
          www.koralinrealestate.com.au
        </div>
      </div>
    </div>
    <div class="flyer__photo" role="img" aria-label="Photo of a smiling real estate agent in a dark suit and glasses seated at a desk in a bright office"></div>
  </section>
</body>
</html>
```